Brightleaf Plots LLC business card

I created a front and back idea of what I want. Also I included my Brightleaf Plots logo to be used on the card. Please use your creativity to make it look professional and awesome! Use the all text and phrases in the sample card that I made.

(Front of card)Key words and phrases:
FOOD GROWING MACHINES
Aeroponics Technology
No soil
No pesticides
98% less water
Grow year round

(Back of card)
EVERY MONTH ONE SPIRE PLANTER WILL BE GIVEN AWAY
FOLLOW US ON IG FOR A CHANCE TO WIN A SPIRE PLANTER
FOOD GROWING MACHINES
Vertical Farming
Urban Farming
100% Organic
Grows 40% Faster
Indoors/outdoors

My contact info:
Chef Morv
Phone:555 417-3290
web: brightleafplots.example
IG: brightleafplotsxy

Target Market(s)

urban farming, vertical farming gardening

Industry/Entity Type

Gardening

Contact Information for Business Card

Front of card)Key words and phrases:
FOOD GROWING MACHINES
Aeroponics Technology
No soil
No pesticides
98% less water
Grow year round

(Back of card)
FOOD GROWING MACHINES
Vertical Farming
Urban Farming
100% Organic
Grows 40% Faster
Indoors/outdoors

My contact info:
Phone:555 417-3290
web: brightleafplots.example
IG: brightleafplotsxy

Requirements
Must have
• My contact info:
Chef Morv
Phone:555 417-3290
web: brightleafplots.example
IG: brightleafplotsxy
Nice to have
• Great imagery and easy to read. Try to incorporate the image that I uploaded of the little girl.

```html
<!DOCTYPE html>
<html lang="en">
<head>
<meta charset="utf-8">
<title>Brightleaf Plots LLC – Business Card</title>
<link href="https://fonts.googleapis.com/css2?family=Fira+Sans:ital,wght@0,400;0,500;0,800;1,500&display=swap" rel="stylesheet">
<style>
  :root {
    --stage: #1c1c1c;
    --blue-light: #6078d2;
    --blue-deep: #3f55b4;
    --leaf-lime: #9fd43a;
    --leaf-green: #4e9a1e;
    --leaf-dark: #3f7f1a;
    --cream: #fbfdf3;
    --cream-edge: #e4f1bf;
    --band: #8cc63f;
    --text-green: #4b8a22;
    --white: #ffffff;
  }
  * { box-sizing: border-box; margin: 0; padding: 0; }
  html, body { width: 1200px; height: 1200px; overflow: hidden; }
  body {
    background: var(--stage);
    font-family: "Fira Sans", sans-serif;
    display: flex;
    flex-direction: column;
    align-items: center;
    justify-content: center;
    gap: 56px;
  }
  .card {
    position: relative;
    width: 880px;
    height: 503px;
    border-radius: 6px;
    overflow: hidden;
    box-shadow: 0 10px 30px rgba(0,0,0,.45);
  }
  .leaf-art {
    position: absolute;
    border-radius: 50% 50% 50% 50% / 60% 60% 40% 40%;
    background: radial-gradient(ellipse at 45% 40%, var(--leaf-lime) 0%, var(--leaf-green) 65%, var(--leaf-dark) 100%);
  }

  /* Back card */
  .card--back {
    background: radial-gradient(ellipse at 40% 60%, var(--white) 0%, var(--cream) 45%, var(--cream-edge) 100%);
  }
  .card--back .leaf-art { left: 50px; top: 120px; width: 310px; height: 200px; }
  .card--back .band {
    position: absolute; left: 0; right: 0; bottom: 0; height: 26px;
    background: linear-gradient(90deg, var(--band), #c6e86a);
  }
  .back-content {
    position: absolute; left: 400px; top: 56px; right: 30px;
    color: var(--text-green);
  }
  .giveaway { font-style: italic; font-weight: 500; font-size: 16px; line-height: 1.4; white-space: nowrap; }
  .contact-line {
    display: flex; align-items: center; gap: 8px;
    font-weight: 500; font-size: 21px; margin-top: 10px;
    white-space: nowrap;
  }
  .contact-name { font-weight: 500; font-size: 21px; margin-top: 12px; white-space: nowrap; }
  .ig-square { width: 18px; height: 18px; border: 2.5px solid var(--text-green); border-radius: 5px; flex: none; }
  .web-dot { width: 16px; height: 16px; border-radius: 50%; background: var(--text-green); flex: none; }
  .service-title {
    font-weight: 500; font-size: 24px; margin-top: 22px;
    padding-bottom: 6px; border-bottom: 1.5px solid var(--text-green); display: inline-block;
  }
  .service-list { list-style: none; margin-top: 12px; font-size: 18px; line-height: 1.7; white-space: nowrap; }
  .service-list .star { color: var(--band); margin: 0 6px; }

  /* Front card */
  .card--front {
    background: linear-gradient(120deg, var(--blue-deep) 0%, var(--blue-light) 55%, var(--blue-deep) 100%);
  }
  .card--front .leaf-art { left: 50px; top: 110px; width: 340px; height: 220px; }
  .brand-name {
    position: absolute; left: 430px; top: 90px;
    font-weight: 800; font-size: 56px; line-height: 0.95; color: var(--leaf-lime);
    text-transform: uppercase; letter-spacing: 1px;
  }
  .brand-name .line { display: block; white-space: nowrap; }
  .brand-name .mark {
    display: inline-block; width: 30px; height: 30px; border-radius: 50%;
    background: var(--leaf-lime); margin-left: 14px; vertical-align: middle;
  }
  .feature-list {
    position: absolute; left: 440px; top: 228px;
    list-style: none; color: var(--white); font-size: 23px; line-height: 1.65; white-space: nowrap;
  }
  .feature-list .star { color: var(--leaf-lime); margin-right: 12px; font-size: 18px; }
</style>
</head>
<body>

  <section class="card card--back" aria-label="Business card back">
    <div class="leaf-art" role="img" aria-label="Green sprouting leaves illustration"></div>
    <div class="back-content">
      <p class="giveaway">Every Month One Spire Planter Will Be Given Away<br>Follow Us On Ig For A Chance To Win A Spire Planter</p>
      <p class="contact-name">Chef Morv</p>
      <p class="contact-line"><span class="ig-square"></span>brightleafplotsxy</p>
      <p class="contact-line">
        <svg width="18" height="18" viewBox="0 0 24 24" aria-hidden="true"><path fill="#4b8a22" d="M6.6 10.8a15.1 15.1 0 0 0 6.6 6.6l2.2-2.2a1 1 0 0 1 1-.25 11.4 11.4 0 0 0 3.6.57 1 1 0 0 1 1 1V20a1 1 0 0 1-1 1A17 17 0 0 1 3 4a1 1 0 0 1 1-1h3.5a1 1 0 0 1 1 1c0 1.25.2 2.45.57 3.57a1 1 0 0 1-.25 1z"/></svg>
        <span>555 417-3290 |</span><span class="web-dot"></span><span>brightleafplots.example</span>
      </p>
      <h2 class="service-title">OUR SERVICE</h2>
      <ul class="service-list">
        <li><span class="star">★</span>Food Growing Machines <span class="star">★</span>Vertical Farming</li>
        <li><span class="star">★</span>Urban Farming <span class="star">★</span>100% Organic</li>
        <li><span class="star">★</span>Grows 40% Faster <span class="star">★</span>Indoors/outdoors</li>
      </ul>
    </div>
    <div class="band"></div>
  </section>

  <section class="card card--front" aria-label="Business card front">
    <div class="leaf-art" role="img" aria-label="Green sprouting leaves illustration"></div>
    <h1 class="brand-name"><span class="line">Brightleaf</span><span class="line">Plots<span class="mark"></span></span></h1>
    <ul class="feature-list">
      <li><span class="star">★</span>FOOD GROWING MACHINES</li>
      <li><span class="star">★</span>Aeroponics Technology</li>
      <li><span class="star">★</span>No soil | No pesticides</li>
      <li><span class="star">★</span>98% less water | Grow year round</li>
    </ul>
  </section>

</body>
</html>
```